Building company buisness cards

We are looking for a sharp modern new look for our business cards.
We are a New Zealand based company that specialises in house and land packages.
We have attached a photo of the current logo and would like to see if it can be improved somehow if needed.
We are open to any colours but we have chosen green at this stage.
Feel free to change the font and make the logo smarter looking.
Play with the colours and see what looks best.

We want a card that looks so good know one will want to throw it away!

Target Market(s)

Home buyers

Industry/Entity Type

Building

Contact Information for Business Card

Garth Ellery
0219364028
gellery@tidewaterhomecraft.co.nz
tidewaterhomecraft.co.nz

Font styles to use
Serif
Sans Serif

Colors

Designer to choose colors to be used in the design.

Requirements
Must have
• Logo and company name on one side, details on the other side
Nice to have
• Color codes for the original green are HEX #4a8028, RGB(74,128,40), CMYK(42,0,69,50)
• Round corners, Raised and/or spot UV

```html
<!DOCTYPE html>
<html lang="en">
<head>
<meta charset="utf-8">
<title>Tidewater Homecraft – Business Card</title>
<link rel="stylesheet" href="https://fonts.googleapis.com/css2?family=Barlow:wght@700&family=Arimo:wght@400&display=swap">
<style>
  :root {
    --navy: #24355f;
    --white: #ffffff;
    --backdrop: #eceae6;
    --silver-light: #fbfbfb;
    --silver-mid: #e6e6e6;
    --silver-dark: #c9c9c9;
  }
  * { margin: 0; padding: 0; box-sizing: border-box; }
  html, body {
    width: 1200px;
    height: 1139px;
    overflow: hidden;
    background: var(--backdrop);
  }
  .canvas {
    position: relative;
    width: 1200px;
    height: 1139px;
  }
  .card {
    position: absolute;
    width: 768px;
    height: 435px;
    box-shadow: 0 3px 10px rgba(0, 0, 0, 0.22);
    overflow: hidden;
  }
  .card-front {
    left: 177px;
    top: 96px;
    background: var(--navy);
    display: flex;
    flex-direction: column;
    align-items: center;
    justify-content: center;
  }
  .brand-name {
    font-family: "Barlow", "Helvetica Neue", Arial, sans-serif;
    font-weight: 700;
    color: var(--white);
    font-size: 46px;
    letter-spacing: 0.5px;
    margin-top: 40px;
  }
  .card-back {
    left: 284px;
    top: 569px;
    background: linear-gradient(90deg,
      var(--silver-mid) 0%,
      var(--silver-light) 22%,
      var(--silver-mid) 48%,
      var(--silver-light) 70%,
      var(--white) 82%,
      var(--silver-dark) 100%);
  }
  .back-brand {
    position: absolute;
    left: 40px;
    top: 60px;
    font-family: "Barlow", "Helvetica Neue", Arial, sans-serif;
    font-weight: 700;
    color: var(--navy);
    font-size: 20px;
  }
  .person-name {
    position: absolute;
    left: 0;
    width: 768px;
    top: 146px;
    text-align: center;
    padding-left: 30px;
    font-family: "Barlow", "Helvetica Neue", Arial, sans-serif;
    font-weight: 700;
    color: var(--navy);
    font-size: 35px;
  }
  .phone-band {
    position: absolute;
    left: 0;
    top: 208px;
    width: 768px;
    height: 60px;
    background: var(--navy);
    display: flex;
    align-items: center;
    justify-content: center;
    gap: 8px;
    padding-left: 30px;
  }
  .phone-icon { width: 26px; height: 44px; }
  .phone-number {
    font-family: "Barlow", "Helvetica Neue", Arial, sans-serif;
    font-weight: 700;
    color: var(--white);
    font-size: 30px;
    letter-spacing: 0.5px;
  }
  .contact-line {
    position: absolute;
    left: 0;
    width: 768px;
    text-align: center;
    padding-left: 30px;
    font-family: "Arimo", Arial, sans-serif;
    font-weight: 400;
    color: var(--navy);
    font-size: 25px;
  }
  .contact-email { top: 297px; }
  .contact-web { top: 339px; }
</style>
</head>
<body>
<main class="canvas">
  <section class="card card-front" aria-label="Card front">
    <div class="brand-name">Tidewater Homecraft</div>
  </section>

  <section class="card card-back" aria-label="Card back">
    <div class="back-brand">Tidewater Homecraft</div>
    <div class="person-name">Garth Ellery</div>
    <div class="phone-band">
      <svg class="phone-icon" viewBox="0 0 26 44" aria-hidden="true">
        <rect x="2" y="2" width="22" height="40" rx="4" fill="none" stroke="#ffffff" stroke-width="3"/>
        <line x1="10" y1="37" x2="16" y2="37" stroke="#ffffff" stroke-width="2.5" stroke-linecap="round"/>
      </svg>
      <span class="phone-number">0219364028</span>
    </div>
    <div class="contact-line contact-email">gellery@tidewaterhomecraft.co.nz</div>
    <div class="contact-line contact-web">tidewaterhomecraft.co.nz</div>
  </section>
</main>
</body>
</html>
```